delivery service for warm food for kids and other kids stuff

plumwicks.nl > daycare website

plumwicks.shop >>> cartloom site we ask you to design!

We are a daycare center and thanks to corona found that we could help parents and kids while at home ! we would like some help to get an awesome and clear site for this.

it doesnt have to look kiddy...
more proffessional and sleek
we love quince website... so anything in that direction would be great!... ie pic next to text...
2 tone colors
ours are pink light blue and white.. so play with that?
black and white also fine!

Target Market(s)

expats and proffesional parents ... so NOT KIDDY website...

Font styles to use
Sans Serif

Requirements
Must have
• sexy design....
simplicity...
less text... more pictures
cool headlines
Should not have
• lots of text everyhwere
busy

```html
<!DOCTYPE html>
<html lang="en">
<head>
<meta charset="utf-8">
<title>Plumwicks Shop</title>
<link href="https://fonts.googleapis.com/css2?family=Poppins:wght@400;500;600&family=Lora:wght@500&display=swap" rel="stylesheet">
<style>
:root{
  --blue:#08a7d9;
  --blue-soft:#a9d3e2;
  --pink:#e2456f;
  --pink-soft:#f3b6c6;
  --grey-card:#d9d9d9;
  --ink:#222;
  --text:#444;
  --white:#fff;
}
*{margin:0;padding:0;box-sizing:border-box}
html,body{width:1200px;height:3599px;overflow:hidden}
body{position:relative;font-family:'Poppins',sans-serif;color:var(--text);background:var(--white)}
.abs{position:absolute}
.brand-badge{position:absolute;border-radius:50%;background:var(--white);border:3px solid var(--blue);display:flex;align-items:center;justify-content:center;text-align:center;color:var(--pink);font-weight:600;line-height:1.05}

/* nav */
.topbar{left:0;top:0;width:1200px;height:63px;background:var(--blue)}
.topbar .brand-badge{left:120px;top:5px;width:52px;height:52px;font-size:10px;border-color:var(--white)}
.nav-links{position:absolute;left:305px;top:21px;display:flex;gap:26px;font-size:14px;font-weight:500;color:var(--white)}
.nav-icon{position:absolute;top:19px}

/* hero */
.hero{left:0;top:63px;width:1200px;height:480px;background:linear-gradient(100deg,#5a4a3c 0%,#7a6453 35%,#8f7866 55%,#5e5046 80%,#3f3731 100%)}
.hero .brand-badge{left:120px;top:18px;width:76px;height:76px;font-size:13px;border-width:3px}
.hero-title{left:0;width:1200px;top:158px;text-align:center;color:var(--white);font-size:35px;font-weight:500}
.hero-sub{left:0;width:1200px;top:202px;text-align:center;color:var(--white);font-size:17px}
.hero-btn{left:532px;top:237px;width:136px;height:38px;border:2px solid var(--white);border-radius:19px;color:var(--white);font-size:10px;display:flex;align-items:center;justify-content:center}

/* intro */
.intro-title{left:119px;top:790px;font-size:28px;color:var(--blue);font-weight:500}
.intro-text{left:119px;top:828px;width:580px;font-size:13.6px;line-height:23.3px;color:var(--text)}
.intro-badge{left:831px;top:802px;width:246px;height:246px;font-size:38px;border-width:6px}

/* testimonials */
.section-title{left:0;width:1200px;text-align:center;color:var(--blue);font-weight:500}
.reviews{left:0;top:1316px;width:1200px;height:479px;background:var(--blue)}
.review-side{top:113px;width:164px;height:245px;background:var(--blue-soft);border-radius:6px;overflow:hidden}
.review-main{left:426px;top:87px;width:351px;height:307px;background:var(--grey-card);border-radius:6px}
.avatar{position:absolute;border-radius:50%;background:linear-gradient(180deg,#9a9a9a,#4d4d4d)}
.quote-mark{position:absolute;color:var(--pink);font-family:'Lora',serif;font-size:44px;line-height:1}
.review-text{position:absolute;font-family:'Lora',serif;color:var(--ink)}
.dots{position:absolute;display:flex;gap:5px}
.dots i{width:4px;height:4px;border-radius:50%;background:#222;display:block}
.dots i.on{background:var(--pink)}

/* products */
.card{top:2114px;width:240px;height:359px;background:var(--white);border-radius:16px;box-shadow:0 3px 0 #bfe6f3,0 0 0 1px #e6f5fa;overflow:hidden}
.card.hover{box-shadow:0 0 0 2px var(--pink-soft)}
.card-img{position:absolute;left:30px;top:65px;width:180px;height:175px}
.card-name{position:absolute;left:0;width:100%;top:257px;text-align:center;font-size:13px;font-weight:600}
.card-desc{position:absolute;left:0;width:100%;top:275px;text-align:center;font-size:10px;color:#555}
.price{position:absolute;left:80px;top:299px;width:80px;height:22px;border-radius:11px;border:2px solid;font-size:10px;font-weight:600;display:flex;align-items:center;justify-content:center}
.ribbon{position:absolute;right:0;top:0}
.faded{opacity:.35}
.qty{position:absolute;left:30px;top:148px;height:30px;border:2px solid var(--pink);border-radius:15px;color:var(--pink);font-size:14px;display:flex;align-items:center}
.btn{height:48px;border-radius:24px;font-size:14px;font-weight:500;display:flex;align-items:center;justify-content:center}

/* courses */
.courses{left:0;top:2766px;width:1200px;height:400px;background:linear-gradient(90deg,#0aa6d8 0%,#2f94bf 40%,#4a7b96 70%,#3b5566 100%)}
.courses-title{left:120px;top:125px;color:var(--white);font-size:24px;font-weight:600}
.courses-text{left:120px;top:160px;width:560px;color:var(--white);font-size:13px;line-height:20px}
.courses-btn{left:120px;top:231px;width:143px;height:46px;background:var(--white);color:var(--blue);border-radius:23px;font-size:13px;font-weight:500;display:flex;align-items:center;justify-content:center}

/* footer */
.footer-badge{left:544px;top:3379px;width:112px;height:112px;font-size:18px}
.footer-links{left:0;width:1200px;top:3503px;display:flex;justify-content:center;gap:41px;font-size:17px;color:var(--text);text-transform:uppercase}
.social{top:3543px;width:30px;height:30px;border-radius:6px;background:var(--blue)}
.footer-strip{left:0;top:3593px;width:1200px;height:6px;background:var(--blue)}
</style>
</head>
<body>

<header class="abs topbar">
  <div class="brand-badge">Plumwicks<br>Shop</div>
  <nav class="nav-links"><span>Home</span><span>Warm Food</span><span>Drinks</span><span>Flowers</span><span>Heathy Bars</span><span>Puzzel Mats</span><span>Courses</span></nav>
  <svg class="nav-icon" style="left:956px;top:23px" width="17" height="17" viewBox="0 0 17 17"><circle cx="7" cy="7" r="5" fill="none" stroke="#fff" stroke-width="2"/><line x1="11" y1="11" x2="15" y2="15" stroke="#fff" stroke-width="2"/></svg>
  <svg class="nav-icon" style="left:1003px" width="26" height="26" viewBox="0 0 26 26"><circle cx="13" cy="13" r="11.5" fill="none" stroke="#fff" stroke-width="1.6"/><circle cx="13" cy="10" r="4" fill="none" stroke="#fff" stroke-width="1.6"/><path d="M5.5 21c2-4 13-4 15 0" fill="none" stroke="#fff" stroke-width="1.6"/></svg>
  <svg class="nav-icon" style="left:1054px" width="28" height="24" viewBox="0 0 28 24"><path d="M1 2h5l3 13h14l3-9H8" fill="none" stroke="#fff" stroke-width="1.6"/><circle cx="11" cy="20" r="2" fill="#fff"/><circle cx="21" cy="20" r="2" fill="#fff"/></svg>
</header>

<section class="abs hero" role="img" aria-label="Photo of a mother with a baby and a toddler using a tablet on a sofa">
  <div class="brand-badge">Plumwicks<br>Shop</div>
  <h1 class="abs hero-title">Welcome to Plumwicks Shop.</h1>
  <p class="abs hero-sub">We will help parents in these hard times of pandemic by providing goodies for an affordable price.</p>
  <div class="abs hero-btn">Browse Products</div>
</section>

<section>
  <h2 class="abs intro-title">In this time of Pandemic...</h2>
  <p class="abs intro-text">Lorem ipsum dolor sit amet, consectetur adipisicing elit, sed do eiusmod tempor incididunt ut labore et dolore magna aliqua. Ut enim ad minim veniam, quis nostrud exercitation ullamco laboris nisi ut aliquip ex ea commodo consequat. Duis aute irure dolor in reprehenderit in voluptate velit esse cillum dolore eu fugiat nulla pariatur. Excepteur sint occaecat cupidatat non proident, sunt in culpa qui officia deserunt mollit anim id est laborum. Sed ut perspiciatis unde omnis iste natus error sit voluptatem accusantium doloremque laudantium, totam rem aperiam, eaque ipsa quae ab illo inventore veritatis et quasi architecto beatae vitae dicta sunt explicabo. Nemo enim ipsam voluptatem quia voluptas sit aspernatur aut odit aut fugit, sed quia conse-</p>
  <div class="brand-badge intro-badge">Plumwicks<br>Shop</div>
</section>

<h2 class="abs section-title" style="top:1250px;font-size:28px">Our buyers said</h2>
<section class="abs reviews">
  <div class="abs review-side" style="left:263px">
    <div class="avatar" style="left:112px;top:22px;width:50px;height:50px" role="img" aria-label="Buyer portrait"></div>
    <div class="quote-mark" style="left:128px;top:86px;font-size:32px">“</div>
    <p class="review-text" style="left:27px;top:122px;width:150px;font-size:10.5px;line-height:16px;white-space:nowrap">Lorem ipsum dolor sit amet<br>isicing elit, sed do eiusmod<br>ut labore et dolore magna a<br>minim veniam, quis nostru</p>
    <div class="abs" style="left:127px;top:198px;font-size:5px">JOHN DOE</div>
    <div class="dots" style="left:130px;top:231px"><i></i><i class="on"></i><i></i></div>
  </div>
  <div class="abs review-side" style="left:772px">
    <div class="avatar" style="left:2px;top:22px;width:50px;height:50px" role="img" aria-label="Buyer portrait"></div>
    <div class="quote-mark" style="left:10px;top:86px;font-size:32px">“</div>
    <p class="review-text" style="left:6px;top:122px;font-size:10.5px;line-height:16px;white-space:nowrap">sit amet, consectetur adip-<br>iusmod tempor incididunt<br>magna aliqua. Ut enim ad<br>nostrud exercitation ulla-</p>
    <div class="abs" style="left:6px;top:198px;font-size:5px">JOHN DOE</div>
    <div class="dots" style="left:12px;top:231px"><i></i><i class="on"></i><i></i></div>
  </div>
  <div class="abs review-main">
    <svg class="abs" style="left:75px;top:53px" width="12" height="16"><path d="M9 2 3 8l6 6" fill="none" stroke="#e2456f" stroke-width="2"/></svg>
    <svg class="abs" style="left:263px;top:53px" width="12" height="16"><path d="M3 2l6 6-6 6" fill="none" stroke="#e2456f" stroke-width="2"/></svg>
    <div class="avatar" style="left:138px;top:24px;width:74px;height:74px" role="img" aria-label="Buyer portrait"></div>
    <div class="quote-mark" style="left:158px;top:110px">“</div>
    <p class="review-text" style="left:34px;top:150px;width:290px;font-size:13px;line-height:20px">Lorem ipsum dolor sit amet, consectetur adipisicing elit, sed do eiusmod tempor incididunt ut labore et dolore magna aliqua. Ut enim ad minim veniam, quis nostrud exercitation ulla-</p>
    <div class="abs" style="left:0;width:100%;top:243px;text-align:center;font-size:6px;color:#222">JOHN DOE</div>
    <div class="abs" style="left:0;width:100%;top:254px;text-align:center;font-size:5px;color:#888">BUYER</div>
    <div class="dots" style="left:164px;top:287px"><i></i><i class="on"></i><i></i></div>
  </div>
</section>

<h2 class="abs section-title" style="top:1966px;font-size:30px">Featured Products</h2>

<svg class="abs" style="left:26px;top:2310px" width="28" height="52"><path d="M25 2 3 26l22 24" fill="none" stroke="#08a7d9" stroke-width="2.5"/></svg>
<svg class="abs" style="left:1146px;top:2310px" width="28" height="52"><path d="M3 2l22 24L3 50" fill="none" stroke="#08a7d9" stroke-width="2.5"/></svg>

<div class="abs card" style="left:98px">
  <div class="card-img" style="background:linear-gradient(180deg,#e8f3fa,#b9d8ec)" role="img" aria-label="Two bottles of still water"></div>
  <div class="card-name" style="color:var(--blue)">Water</div>
  <div class="card-desc">nisi ut aliquip ex ea commodo</div>
  <div class="price" style="color:var(--blue);border-color:var(--blue)">€2,00</div>
</div>

<div class="abs card hover" style="left:353px">
  <div class="faded">
    <div class="card-img" style="background:linear-gradient(160deg,#8d7d9e,#6f8a5a)" role="img" aria-label="Bowl of pea stew with chicken"></div>
    <div class="card-name" style="color:var(--pink)">Pea stew with chicken</div>
    <div class="card-desc">nisi ut aliquip ex ea commodo</div>
    <div class="price" style="color:var(--pink);border-color:var(--pink)">€4,00</div>
  </div>
  <div class="qty" style="width:104px;padding-left:14px">2</div>
  <svg class="abs" style="left:138px;top:148px" width="30" height="30"><circle cx="15" cy="15" r="13.5" fill="#fff" stroke="#e2456f" stroke-width="2"/><path d="M9 15h12M15 9v12" stroke="#e2456f" stroke-width="2.4"/></svg>
  <svg class="abs" style="left:174px;top:148px" width="30" height="30"><circle cx="15" cy="15" r="13.5" fill="#fff" stroke="#e2456f" stroke-width="2"/><path d="M9 15h12" stroke="#e2456f" stroke-width="2.4"/></svg>
  <div class="qty" style="top:186px;width:178px;justify-content:center">Add to Cart</div>
</div>

<div class="abs card" style="left:608px">
  <svg class="ribbon" width="102" height="60"><path d="M0 0h102v60z" fill="#08a7d9"/><text x="74" y="22" fill="#fff" font-family="Poppins,sans-serif" font-size="12" font-weight="600" text-anchor="middle">New</text></svg>
  <div class="card-img" style="background:linear-gradient(160deg,#dfe6e0,#c45a72 60%,#e9e3c9)" role="img" aria-label="Glasses of berry smoothie with straws"></div>
  <div class="card-name" style="color:var(--pink)">Smoothie</div>
  <div class="card-desc">nisi ut aliquip ex ea commodo</div>
  <div class="price" style="color:var(--pink);border-color:var(--pink)">€3,25</div>
</div>

<div class="abs card" style="left:862px">
  <svg class="ribbon" width="102" height="60"><path d="M0 0h102v60z" fill="#08a7d9"/><text x="74" y="22" fill="#fff" font-family="Poppins,sans-serif" font-size="12" font-weight="600" text-anchor="middle">New</text></svg>
  <div class="card-img" style="top:75px;height:155px;background:linear-gradient(160deg,#5d3f58,#3f6b37 55%,#d8344f)" role="img" aria-label="Fruit and nut bar lying among flowers"></div>
  <div class="card-name" style="color:var(--pink)">Nutly Vegan Bars</div>
  <div class="card-desc">nisi ut aliquip ex ea commodo</div>
  <div class="price" style="color:var(--pink);border-color:var(--pink)">€1,75</div>
</div>

<div class="abs btn" style="left:437px;top:2515px;width:158px;background:var(--blue);color:var(--white)">Browse Products</div>
<div class="abs btn" style="left:603px;top:2515px;width:158px;border:2px solid var(--pink);color:var(--pink)">Checkout</div>

<section class="abs courses" role="img" aria-label="Blurred library bookshelves under a blue tint">
  <h2 class="abs courses-title">Why not gain more skills in this time of lockdown ?</h2>
  <p class="abs courses-text">Lorem ipsum dolor sit amet, consectetur adipisicing elit, sed do eiusmod tempor incididunt ut labore et dolore magna aliqua. Ut enim ad minim veniam, quis nostrud exercitation ullamco laboris nisi ut aliquip ex ea commodo consequat. Duis aute irure</p>
  <div class="abs courses-btn">Browse Courses</div>
</section>

<footer>
  <div class="brand-badge footer-badge">Plumwicks<br>Shop</div>
  <nav class="abs footer-links"><span>Home</span><span>Warm Food</span><span>Drinks</span><span>Flowers</span><span>Heathy Bars</span><span>Puzzel Mats</span><span>Courses</span></nav>
  <div class="abs social" style="left:546px" role="img" aria-label="Social profile link"></div>
  <div class="abs social" style="left:590px" role="img" aria-label="Social profile link"></div>
  <div class="abs social" style="left:636px" role="img" aria-label="Social profile link"></div>
  <div class="abs footer-strip"></div>
</footer>

</body>
</html>
```